Web Banners

I need banners to run ads in Chatterloop and vexmora ads. No flash needed. Just static or animated as you see fit.

Our website: www.brinelarkretreats.com
The banners will be promoting our surf camps in Boca and Deerfield as "Brinelark Retreats".

I will be using this 3rd party site to list my ads. Here are their full requirements:
http://support.pixelwren.com/creative-requirements/

These are the banners I need
- Banner – 468×60
- Square – 250×250
- Small Square – 200×200
- Leaderboard – 728×90
- Medium Rectangle – 300×250
- Large Rectangle – 336×280
- Skyscraper – 120×600
- Wide Skyscraper – 160×600
- Mobile Leaderboard – 320×50
- Chatterloop – 100×72
- Chatterloop Story Stream – 200×200, 600×315

For proofing purposes, if you want to do 1 or 2 in the beginning, that's fine.
Once we approve your direction, I would need the remaining banners before final payment is made. I have included some graphics to get you started.

Key focus for any statements would be:
learn from pro surfers
make new friends
learn how to surf
improve your surfing skills

```html
<!DOCTYPE html>
<html lang="en">
<head>
<meta charset="utf-8">
<title>Brinelark Retreats – Web Banners</title>
<link href="https://fonts.googleapis.com/css2?family=Roboto+Condensed:wght@300;400;700&display=swap" rel="stylesheet">
<style>
:root{
  --stage:#2e2e2e;
  --teal:#4fa39b;
  --teal-dark:#3a8580;
  --teal-light:#6cc2b9;
  --stripe:#8fe0d8;
  --photo-top:#e4eeeb;
  --photo-mid:#b7d4cf;
  --photo-low:#7fb2ab;
  --water-top:#cfe3df;
  --water-bottom:#8cbcb5;
  --white:#ffffff;
  --ink:#111111;
  --btn-top:#ffd92a;
  --btn-bottom:#f19400;
  --btn-text:#1d1d1d;
  --headline:#ffffff;
}
*{margin:0;padding:0;box-sizing:border-box}
html,body{width:1200px;height:797px;overflow:hidden;background:var(--stage)}
body{position:relative;font-family:"Roboto Condensed",Arial,sans-serif}

.banner{position:absolute;overflow:hidden;
  background:linear-gradient(90deg,var(--teal-dark),var(--teal) 40%,var(--teal-light) 70%,var(--teal));}

.photo{position:absolute;
  background:linear-gradient(180deg,var(--photo-top) 0%,var(--photo-mid) 50%,var(--photo-low) 100%);
  box-shadow:inset 0 0 0 1px rgba(255,255,255,.35)}
.photo--water{background:linear-gradient(180deg,var(--water-top),var(--water-bottom))}

.headline{position:absolute;z-index:2;color:var(--headline);font-weight:700;text-transform:uppercase;
  text-align:center;line-height:1.02;text-shadow:0 1px 3px rgba(0,0,0,.35)}
.headline .small{font-size:.78em}

.logo-box{position:absolute;background:var(--white);display:flex;align-items:center;justify-content:center}
.logo{display:flex;align-items:center;gap:7px;color:var(--ink);font-weight:300;text-transform:uppercase;line-height:.95}
.logo--overlay{position:absolute;z-index:2}
.logo__name{display:block}
.logo__dot{border-radius:50%;background:var(--ink);flex:none}

.cta{position:absolute;z-index:3;display:flex;align-items:center;justify-content:center;gap:8px;
  border-radius:4px;background:linear-gradient(180deg,var(--btn-top),var(--btn-bottom));
  color:var(--btn-text);font-size:19px;font-weight:400;box-shadow:0 2px 3px rgba(0,0,0,.35)}
.cta svg{flex:none}
.stripe{position:absolute;left:0;right:0;height:6px;background:linear-gradient(90deg,var(--teal),var(--stripe),var(--teal))}
</style>
</head>
<body>

<!-- Wide skyscraper -->
<section class="banner" style="left:65px;top:124px;width:155px;height:580px">
  <div class="logo-box" style="left:0;top:0;width:155px;height:67px">
    <div class="logo" style="font-size:19px"><span><span class="logo__name">Brinelark</span><span class="logo__name">Retreats</span></span><span class="logo__dot" style="width:26px;height:26px"></span></div>
  </div>
  <div class="stripe" style="top:67px"></div>
  <h2 class="headline" style="left:0;width:155px;top:84px;font-size:31px">Improve<br>your<br>surfing<br>skills</h2>
  <div class="photo photo--water" role="img" aria-label="Shallow ocean water with a teal surfboard" style="left:0;top:420px;width:155px;height:160px"></div>
  <div class="photo" role="img" aria-label="Smiling boy giving thumbs up while standing on a surfboard" style="left:12px;top:210px;width:130px;height:340px"></div>
  <a class="cta" style="left:8px;top:535px;width:138px;height:34px">Click Now <svg width="20" height="20" viewBox="0 0 20 20"><circle cx="10" cy="10" r="9" fill="#eee" stroke="#999"/><path d="M8 5l5 5-5 5" fill="none" stroke="#222" stroke-width="2.4"/></svg></a>
</section>

<!-- Skyscraper -->
<section class="banner" style="left:238px;top:124px;width:155px;height:580px">
  <div class="logo-box" style="left:0;top:0;width:155px;height:67px">
    <div class="logo" style="font-size:19px"><span><span class="logo__name">Brinelark</span><span class="logo__name">Retreats</span></span><span class="logo__dot" style="width:26px;height:26px"></span></div>
  </div>
  <div class="stripe" style="top:67px"></div>
  <h2 class="headline" style="left:0;width:155px;top:84px;font-size:31px">Improve<br>your<br>surfing<br>skills</h2>
  <div class="photo photo--water" role="img" aria-label="Shallow ocean water with a white surfboard" style="left:0;top:390px;width:155px;height:190px"></div>
  <div class="photo" role="img" aria-label="Boy in white shirt standing on a surfboard" style="left:15px;top:212px;width:125px;height:320px"></div>
  <a class="cta" style="left:8px;top:535px;width:138px;height:34px">Click Now <svg width="20" height="20" viewBox="0 0 20 20"><circle cx="10" cy="10" r="9" fill="#eee" stroke="#999"/><path d="M8 5l5 5-5 5" fill="none" stroke="#222" stroke-width="2.4"/></svg></a>
</section>

<!-- Large rectangle A -->
<section class="banner" style="left:449px;top:124px;width:325px;height:270px">
  <div class="photo photo--water" role="img" aria-label="Ocean water with a child paddling a yellow surfboard" style="left:0;top:150px;width:325px;height:120px"></div>
  <div class="photo" role="img" aria-label="Boy giving thumbs up while standing on a teal surfboard" style="left:20px;top:8px;width:150px;height:225px"></div>
  <h2 class="headline" style="left:150px;width:175px;top:22px;font-size:33px">Improve<br><span class="small">your surfing</span><br>skills</h2>
  <div class="logo logo--overlay" style="left:10px;top:220px;font-size:20px"><span><span class="logo__name">Brinelark</span><span class="logo__name">Retreats</span></span><span class="logo__dot" style="width:30px;height:30px"></span></div>
  <a class="cta" style="left:171px;top:226px;width:145px;height:37px">Click Now <svg width="20" height="20" viewBox="0 0 20 20"><circle cx="10" cy="10" r="9" fill="#eee" stroke="#999"/><path d="M8 5l5 5-5 5" fill="none" stroke="#222" stroke-width="2.4"/></svg></a>
</section>

<!-- Large rectangle B -->
<section class="banner" style="left:785px;top:124px;width:325px;height:270px">
  <div class="photo photo--water" role="img" aria-label="Shoreline with palm trees and shallow water" style="left:0;top:130px;width:325px;height:140px"></div>
  <div class="photo" role="img" aria-label="Boy standing on a white surfboard in shallow water" style="left:198px;top:12px;width:105px;height:235px"></div>
  <h2 class="headline" style="left:8px;width:190px;top:18px;font-size:33px">Improve<br><span class="small">your surfing</span><br>skills</h2>
  <div class="logo logo--overlay" style="left:20px;top:158px;font-size:21px"><span><span class="logo__name">Brinelark</span><span class="logo__name">Retreats</span></span><span class="logo__dot" style="width:32px;height:32px"></span></div>
  <a class="cta" style="left:27px;top:218px;width:145px;height:37px">Click Now <svg width="20" height="20" viewBox="0 0 20 20"><circle cx="10" cy="10" r="9" fill="#eee" stroke="#999"/><path d="M8 5l5 5-5 5" fill="none" stroke="#222" stroke-width="2.4"/></svg></a>
</section>

<!-- Leaderboard 1 -->
<section class="banner" style="left:428px;top:419px;width:703px;height:87px">
  <div class="logo-box" style="left:0;top:0;width:172px;height:87px">
    <div class="logo" style="font-size:21px"><span><span class="logo__name">Brinelark</span><span class="logo__name">Retreats</span></span><span class="logo__dot" style="width:32px;height:32px"></span></div>
  </div>
  <div class="photo photo--water" role="img" aria-label="Surfer's legs on a teal board and a child paddling a yellow board" style="left:430px;top:0;width:273px;height:87px"></div>
  <h2 class="headline" style="left:180px;width:250px;top:8px;font-size:34px">Improve your<br>surfing skills</h2>
  <a class="cta" style="left:548px;top:24px;width:148px;height:36px">Click Now <svg width="20" height="20" viewBox="0 0 20 20"><circle cx="10" cy="10" r="9" fill="#eee" stroke="#999"/><path d="M8 5l5 5-5 5" fill="none" stroke="#222" stroke-width="2.4"/></svg></a>
</section>

<!-- Leaderboard 2 -->
<section class="banner" style="left:428px;top:519px;width:703px;height:87px">
  <div class="logo-box" style="left:0;top:0;width:172px;height:87px">
    <div class="logo" style="font-size:21px"><span><span class="logo__name">Brinelark</span><span class="logo__name">Retreats</span></span><span class="logo__dot" style="width:32px;height:32px"></span></div>
  </div>
  <div class="photo" role="img" aria-label="Smiling boy giving thumbs up in a surf camp shirt" style="left:432px;top:0;width:110px;height:87px"></div>
  <h2 class="headline" style="left:178px;width:250px;top:8px;font-size:34px">Improve your<br>surfing skills</h2>
  <a class="cta" style="left:560px;top:18px;width:148px;height:36px">Click Now <svg width="20" height="20" viewBox="0 0 20 20"><circle cx="10" cy="10" r="9" fill="#eee" stroke="#999"/><path d="M8 5l5 5-5 5" fill="none" stroke="#222" stroke-width="2.4"/></svg></a>
</section>

<!-- Leaderboard 3 -->
<section class="banner" style="left:428px;top:616px;width:703px;height:87px">
  <div class="logo-box" style="left:0;top:0;width:172px;height:87px">
    <div class="logo" style="font-size:21px"><span><span class="logo__name">Brinelark</span><span class="logo__name">Retreats</span></span><span class="logo__dot" style="width:32px;height:32px"></span></div>
  </div>
  <div class="photo photo--water" role="img" aria-label="Shallow water with a white surfboard" style="left:440px;top:0;width:263px;height:87px"></div>
  <div class="photo" role="img" aria-label="Boy standing on a white surfboard" style="left:450px;top:0;width:120px;height:87px"></div>
  <h2 class="headline" style="left:185px;width:250px;top:8px;font-size:34px">Improve your<br>surfing skills</h2>
  <a class="cta" style="left:541px;top:34px;width:148px;height:36px">Click Now <svg width="20" height="20" viewBox="0 0 20 20"><circle cx="10" cy="10" r="9" fill="#eee" stroke="#999"/><path d="M8 5l5 5-5 5" fill="none" stroke="#222" stroke-width="2.4"/></svg></a>
</section>

</body>
</html>
```